Colourful Bold Design for Pet Insurance Website

PLEASE NOTE THAT THIS PROJECT HAS BEEN EXTENDED. Please read the PROJECT EXTENSION DOCUMENT BEFORE STARTING WORK ON ANY DESIGNS.

We are looking for a colourful bold new template design for our JOOMLA HOMEPAGE and a matching design for our new WORDPRESS BLOG.

The website will help pet owners work out which insurance policy best meets their needs. The aim of the website is to explain policy differences in a plain clear manner.

The website will need to have a professional colourful image. It needs to be BOLD, CLEAN AND SHARP rather than soft, pastel and cuddly.

COLOUR SCHEME
The website needs to have a bold colourful design on a white background.
On the inner pages we will have five different types of policies which will be colour coded. We would ideally therefore like to incorporate five distinct colours in the design. See attached document for example of colour schemes we like.

LOGO
We want to keep the existing logo. Please find the file attached. You may though change the logo colours.

CONTENT
One of the reasons for the new design is that we want to change the style of the homepage and include new content. Our current homepage can be found at www.furrow-cover-polls.co.uk.

Content Required
Slideshow
Article Intro.. About Pet Insurance
Policy Lookup Box (see existing site… you can change the design of this)
Six link options (see links on left of current page)
Latest Reviews (List of 6)
Ad (Same dimensions as currently on homepage)

News and Comment Section - To include Three or Four Articles, Title, Intro to article (probably 3 or 4 lines .. about 400px wide), Read more link
Social Media Section
Facebark Plugin with Feed
Latest Tweets Plugin
Pet Charities Latest Tweets
Footer
Larger footer with lots of links grouped in sections

It does not need to include the clipart pic of the pets which is on the current homepage.

Examples of Websites and Templates We Like
http://www.pawlane.com/ (like colours… fonts…layout)
http://sitetheme.brightkiln.com/?template=upbeat&path=/... (like the clarity, "white" space etc)
http://www.layoutforge.com/demo/51872.html (like white space, clear easy to read fonts… don’t like colour scheme, size of top picture)
http://www.layoutforge.com/website-templates/63915.html (like colour scheme, use of white space)

FEEDBACK
I will provide lots of feedback on all designs submitted so that together we can get the best result.

For clarification this is a DESIGN ONLY project. Our website developer will view the designs before we make our final choice as he wants to ensure he can develop "sharp, practical and most importantly light weight web interface" from the design.

Just updated this brief to clarify design issues, content issues and to give some more examples of site designs I like. 

Please note that although we wish to keep the logo you can change the colours to suit your design. 

Please note that we have now added details of pictures we would be happy to use on the website.  We would prefer it if you used one of these.   Otherwise please ensure your picture includes a nice dog and nice cat and no people!

I have been delighted with the quality of the designs submitted for this project.  So much so that I am going to extend the project to include some additional inner pages.   The amended brief will be posted on here on Friday 10 May.   The deadline will be extended and the budget will also be increased. 

Reason: Additional inner pages now required. Budget will be increased. Revised brief to be posted on here Friday 10 May.

Target Market(s)

Pet owners in the UK who are confused about pet insurance. It therefore needs to be a bold design which is plain, clean and easy to read. It should use bold colours rather than pastels and should not use "cuddly" images.

Industry/Entity Type

Insurance

Requirements
Must have
• Bold clear and distinct colours (preferably 5)
Content as per uploaded file (not just content from existing site)
Easy to read fonts
Should not have
• Pastel colours
Cuddly images

```html
<!DOCTYPE html>
<html lang="en">
<head>
<meta charset="utf-8">
<title>Furrow Cover Polls UK</title>
<link href="https://fonts.googleapis.com/css2?family=Open+Sans:wght@400;600;700&family=Oswald:wght@400;500&display=swap" rel="stylesheet">
<style>
:root{
  --navy:#0b2c50;
  --brown:#2d2521;
  --sky:#1ba3df;
  --sky-dark:#0a7fc0;
  --orange:#e8600d;
  --orange-dark:#c94f07;
  --magenta:#c4145a;
  --steel:#6e8c9c;
  --ad:#88bdf4;
  --ink:#333;
  --white:#fff;
}
*{box-sizing:border-box;margin:0;padding:0}
html,body{width:1082px;height:1200px;overflow:hidden;background:var(--white);font-family:"Open Sans",sans-serif;color:var(--ink)}
.page{position:relative;width:1082px;height:1200px;overflow:hidden}
.topbar{position:absolute;left:0;top:0;width:100%;height:39px;background:var(--navy);color:var(--white);font-size:12px;font-weight:600}
.follow{position:absolute;right:26px;top:7px;display:flex;align-items:center;gap:9px}
.follow .dot{width:26px;height:26px;border-radius:50%;background:#e6eef5}
.follow .label{margin-right:14px}
.header{position:absolute;left:0;top:39px;width:100%;height:184px;background:var(--brown)}
.logo{position:absolute;left:125px;top:62px;display:flex;align-items:center;gap:12px}
.logo .mark{width:56px;height:56px;background:var(--sky)}
.logo .name{font-size:28px;font-weight:700;line-height:30px;color:var(--white)}
.lookup{position:absolute;left:563px;top:106px;width:394px;height:70px;background:var(--sky);border-radius:14px 14px 0 0}
.lookup h2{position:absolute;left:26px;top:4px;font-family:"Oswald",sans-serif;font-weight:500;font-size:17px;color:var(--white);letter-spacing:.2px}
.lookup .field{position:absolute;top:28px;width:178px;height:30px;background:var(--white);border-radius:15px;border:2px solid #d7e8f2;font-size:11px;color:#555;padding:7px 12px}
.lookup .field svg{position:absolute;right:10px;top:7px}
.nav{position:absolute;left:115px;top:171px;width:855px;height:58px;background:linear-gradient(#2cb8ee,#0a8fd3);border-radius:6px 6px 0 0;display:flex;justify-content:space-around;align-items:center;padding:0 18px}
.nav a{color:var(--white);text-decoration:none;font-size:13px;display:flex;flex-direction:column;align-items:center;gap:3px}
.hero-band{position:absolute;left:0;top:223px;width:100%;height:368px;background:radial-gradient(ellipse at 50% 45%,#9fb4bf 0%,#6f8b99 55%,#4d6a79 100%)}
.slide{position:absolute;left:115px;top:245px;width:854px;height:313px;border:5px solid var(--white);background:linear-gradient(100deg,#dfe7ec 0%,#c6d6e2 45%,#9cc3e4 70%,#86b24e 100%)}
.slide .photo{position:absolute;right:0;top:0;width:420px;height:303px;background:linear-gradient(160deg,#8bb8e4 0%,#b9cfe0 45%,#5b4634 70%,#9a8a6a 88%,#7ea346 100%)}
.slide h1{position:absolute;left:18px;top:38px;font-family:"Oswald",sans-serif;font-weight:400;font-size:28px;color:#222}
.slide .tag{position:absolute;left:12px;height:27px;padding:2px 8px;font-size:18px;color:var(--white)}
.tag.blue{top:88px;background:var(--sky)}
.tag.orange{top:122px;background:var(--orange)}
.tag.magenta{top:156px;background:var(--magenta)}
.dots{position:absolute;left:33px;top:268px;display:flex;gap:4px}
.dots i{width:14px;height:14px;border-radius:50%;background:var(--sky)}
.dots i:first-child{background:var(--magenta)}
.services{position:absolute;left:117px;top:602px;width:245px;height:600px;border:3px solid #e2e2e2;border-radius:14px;background:var(--orange);padding:50px 12px 0}
.services .cap{position:absolute;left:42px;top:-6px;width:155px;height:40px;background:var(--sky);border-radius:0 0 18px 18px;font-family:"Oswald",sans-serif;font-weight:500;font-size:17px;color:#0b2c50;text-align:center;line-height:38px}
.service{color:var(--white);border-bottom:2px solid var(--orange-dark);padding-bottom:11px;margin-bottom:11px}
.service h3{font-size:16px;font-weight:600;line-height:20px;margin-bottom:4px}
.service p{font-size:11px;line-height:15px}
.service:last-child{border:none}
.intro{position:absolute;left:382px;top:612px;width:359px}
.intro h2{font-size:15px;font-weight:400;color:var(--sky);margin-bottom:12px}
.intro p{font-size:11px;line-height:15px;margin-bottom:15px}
.intro .more{display:block;font-size:10px;font-weight:700;color:#0b2c50;text-decoration:underline;margin:-6px 0 20px}
.box{position:absolute;left:749px;width:220px;background:var(--orange);border:3px solid #e2e2e2;border-radius:10px}
.share{top:597px;height:61px;display:flex;align-items:center;justify-content:center;gap:13px}
.share span{width:26px;height:26px;border-radius:3px;background:#2d7fc1}
.share span.go{background:#2c9a3a}
.share span.ln{background:#1f6aa5}
.search{top:667px;height:60px;padding:0 14px;display:flex;align-items:center}
.search .in{flex:1;min-width:0;height:31px;background:var(--white);border-radius:6px 0 0 6px;font-size:11px;padding:8px 12px;color:#555}
.search .btn{flex:0 0 46px;height:31px;background:var(--magenta);border-radius:0 6px 6px 0;font-size:11px;font-weight:700;color:var(--white);text-align:center;line-height:31px}
.ad{position:absolute;left:749px;top:745px;width:221px;height:221px;background:var(--ad);border:3px solid #2a3946;font-size:15px;line-height:16px;color:#0b2c50;display:flex;align-items:center;justify-content:center;text-align:center}
.reviews{position:absolute;left:749px;top:981px;width:220px;height:240px;background:var(--magenta);border:3px solid #e2e2e2;border-radius:10px;padding:46px 14px 0 14px}
.reviews .cap{position:absolute;left:32px;top:-5px;width:150px;height:36px;background:#f59a1e;border-radius:0 0 16px 16px;font-family:"Oswald",sans-serif;font-weight:500;font-size:16px;color:#3b1a06;text-align:center;line-height:34px}
.reviews li{list-style:none;position:relative;padding-left:16px;color:var(--white);font-size:11px;line-height:15px;margin-bottom:10px}
.reviews li::before{content:"";position:absolute;left:2px;top:4px;border-left:5px solid var(--white);border-top:4px solid transparent;border-bottom:4px solid transparent}
</style>
</head>
<body>
<div class="page">
  <div class="topbar">
    <div class="follow"><span>Follow Us in</span><span class="dot"></span><span class="label">Facebark</span><span class="dot"></span><span>Chirper</span></div>
  </div>

  <div class="header">
    <div class="logo"><span class="mark"></span><span class="name">Furrow Cover<br>Polls UK</span></div>
  </div>

  <div class="lookup">
    <h2>CHECK OUT A POLICY</h2>
    <div class="field" style="left:12px">Select A Company<svg width="14" height="14" viewBox="0 0 14 14"><circle cx="8.5" cy="5.5" r="4" fill="none" stroke="#222" stroke-width="1.6"/><line x1="5.5" y1="8.5" x2="1" y2="13" stroke="#222" stroke-width="2"/></svg></div>
    <div class="field" style="left:198px">Select Policy<svg width="14" height="14" viewBox="0 0 14 14"><circle cx="8.5" cy="5.5" r="4" fill="none" stroke="#222" stroke-width="1.6"/><line x1="5.5" y1="8.5" x2="1" y2="13" stroke="#222" stroke-width="2"/></svg></div>
  </div>

  <nav class="nav">
    <a href="#"><svg width="14" height="13" viewBox="0 0 14 13"><path d="M7 0L0 6h2v7h4V9h2v4h4V6h2z" fill="#fff"/></svg>Home</a>
    <a href="#"><svg width="11" height="13" viewBox="0 0 11 13"><path d="M1 1h6l3 3v8H1z" fill="none" stroke="#fff" stroke-width="1.5"/></svg>Policies</a>
    <a href="#"><svg width="14" height="12" viewBox="0 0 14 12"><path d="M0 1q3-1 6.5 1v10Q3 10 0 11zM14 1q-3-1-6.5 1v10q3.5-2 6.5-1z" fill="#fff"/></svg>Glossary</a>
    <a href="#"><svg width="13" height="13" viewBox="0 0 13 13"><circle cx="6.5" cy="6.5" r="6.5" fill="#fff"/><rect x="5.6" y="5.5" width="1.8" height="5" fill="#0a8fd3"/><circle cx="6.5" cy="3.4" r="1.1" fill="#0a8fd3"/></svg>Fact Sheets</a>
    <a href="#"><svg width="14" height="13" viewBox="0 0 14 13"><path d="M7 0l7 3-7 3-7-3zM0 6l7 3 7-3M0 9l7 3 7-3" fill="#fff" stroke="#fff" stroke-width="1"/></svg>Survey Reports</a>
    <a href="#"><svg width="14" height="13" viewBox="0 0 14 13"><ellipse cx="7" cy="5.5" rx="6.5" ry="5" fill="#fff"/><path d="M9 9l3 4-5-3z" fill="#fff"/></svg>News &amp; Comments</a>
    <a href="#"><svg width="14" height="11" viewBox="0 0 14 11"><rect width="14" height="11" fill="#fff"/><path d="M0 0l7 6 7-6" fill="none" stroke="#0a8fd3" stroke-width="1.2"/></svg>Contact Us</a>
  </nav>

  <div class="hero-band"></div>
  <div class="slide">
    <div class="photo" role="img" aria-label="Photo of a large tricolour dog sitting behind a tabby cat on grass under a blue sky"></div>
    <h1>HOW WE CAN HELP YOU?</h1>
    <div class="tag blue">Price Ratings &amp; Surveys »</div>
    <div class="tag orange">Claims Satisfaction Ratings &amp; surveys »</div>
    <div class="tag magenta">Policy Details &amp; Analysis »</div>
    <div class="dots"><i></i><i></i><i></i><i></i><i></i></div>
  </div>

  <aside class="services">
    <div class="cap">OUR SERVICES</div>
    <div class="service"><h3>POLICY FILES</h3><p>Full policy details including type of vet fees cover and limits, ratings, age limits, excess details, benefits and terms analysis</p></div>
    <div class="service"><h3>POLICY SEARCH</h3><p>Exclusive to FCP friends. Search our database of more than 200 policies</p></div>
    <div class="service"><h3>FACT SHEETS</h3><p>Learn about pet insurance. A little knowledge is essential to choosing the right policy</p></div>
    <div class="service"><h3>POLICY LISTINMGS BY TYPE</h3><p>Full lists of continuous policies (aka "lifetime policies), 12- month policies and accident policies.</p></div>
    <div class="service"><h3>CLAIMS SURVEY</h3><p>Made a claim in the last 12 months? Please help us to help others by completing this 2-minute survey</p></div>
    <div class="service"><h3>2013 PRICE SURVEY REPORT</h3><p>Due April 2013.</p></div>
  </aside>

  <main class="intro">
    <h2>Welcome to Furrow Cover Polls UK</h2>
    <p>This is an independent website dedicated to helping you to find the best pet insurance policy for your pet</p>
    <p>Here you will find unbiased detailed information about almost all of the 205 pet insurance policies currently available in the UK (we hope the other 3 will follow shortly!)</p>
    <p>We do NOT sell any pet insurance policies nor do we receive commission from any insurance companies</p>
    <a class="more" href="#">Read More</a>
    <h2>Getting Started</h2>
    <p>If you are new to pet insurance or find the different types of policy confusing then start by reading Pet Insurance - An Introduction.</p>
    <p>If you want more details on a particular policy then use the "Check out a policy" search box which is in the s sidebar. Be sure to look at all three pages (summary, benefits and terms).</p>
    <p>If you want to identify suitable policies then use the detailed search facility to produce a shortlist of policies which meet your criteria</p>
    <a class="more" href="#">Read More</a>
    <h2>And Finally</h2>
    <p>All the information on this website is provided free of charge. We hope you will find it useful when looking for the best pet insurance policy for your pet.</p>
  </main>

  <div class="box share"><span class="go"></span><span></span><span></span><span class="ln"></span>
    <svg width="26" height="20" viewBox="0 0 26 20"><rect x="1" y="1" width="24" height="18" fill="#f4f4f4" stroke="#ccc"/><path d="M1 1l12 10 12-10" fill="none" stroke="#bbb" stroke-width="1.5"/></svg></div>
  <div class="box search"><div class="in">Search</div><div class="btn">Search</div></div>
  <div class="ad">Advertising<br>Space</div>

  <aside class="reviews">
    <div class="cap">LATEST REVIEWS</div>
    <ul>
      <li>Pet Insurance Policies - Know Your Terms</li>
      <li>Pet Insurance – an introduction</li>
      <li>Vet Fees - Policy Types</li>
      <li>Common Policy Terms</li>
      <li>Using Price Comparison Engines</li>
      <li>An idea is born!</li>
    </ul>
  </aside>
</div>
</body>
</html>
```